Bertrand Music Video and Film Production

THE FLYER SHOULD INCLUDE THIS TEXT:

"PROFESSIONAL FILM AND MUSIC VIDEO DIRECTzOR WITH OVER 10 YEARS EXPERIENCE. CLIENT LIST INCLUDES, 714, MARWICK, PALE HARBOURS, BRAMBLEGATE, THE LANTERNS, BLUE OAK, TAMSIN-JO, NELL MARIS, QRV, WILLOWTREE.
HD, SUPER 8, LIVE DVD, PROMO REELS AND VIDEOS ON TIME AND ON BUDGET."

I need to create a flyer/ad that I will use to promote myself and the services I provide.

My name is Bertrand Vellacott and I am a music video clip director and editor that can achieve great results regardless of budgets.

Working with HD and Super 8 vintage film formats to achieve the look you want.

I am a Melbourne based film maker with a huge client list; 714, Marwick, Pale Harbours, Nell Maris, Tamsin-Jo, Bramblegate, The Lanterns, Dominic Plaskett, Willowtree Marketing, QRV and Carrowvale Shire Council.

Black and white classic design. Clean and neat not too busy, almost minimal in a way. Incorpirate my initials to create a logo perhaps.

It needs to appeal and relate to various music genres including; rock, pop, soul, funk, country and folk as I make music videos for artists of many genres.

Feature my website:

www.clipvaultia.com/bertvella

Include my email address

bertrandvellacott@mailzephra.com

Many thanks

Bertrand

Target Market(s)

Music artists and bands performing all sorts of music styles from; rock, soul, funk, pop, country and folk.

Appealing also to band managers, artist representation and record labels/music publishers.

Industry/Entity Type

Artists

Requirements
Must have
• My website and email address and my name. I am a sole trader so i don't have a business name as such, just my name, Bertrand Vellacott.
Should not have
• a picture of me

```html
<!DOCTYPE html>
<html lang="en">
<head>
<meta charset="utf-8">
<title>Bertrand Vellacott – Film and Music Video Director</title>
<link rel="stylesheet" href="https://fonts.googleapis.com/css2?family=Oswald:wght@300;400;600;700&family=Roboto+Condensed:wght@300;400&display=swap">
<style>
  :root {
    --ink: #000000;
    --paper: #ffffff;
    --name-grey: #8d8d8d;
    --mono-light: #e6e6e6;
    --mono-dark: #7a7a7a;
    --frame: #9a9a9a;
  }
  html, body {
    margin: 0;
    padding: 0;
    width: 1200px;
    height: 839px;
    overflow: hidden;
    background: var(--ink);
  }
  .canvas {
    position: relative;
    width: 1200px;
    height: 839px;
    background: var(--ink);
    box-sizing: border-box;
    border: 2px solid var(--frame);
    overflow: hidden;
  }
  /* Portrait flyer laid on its side */
  .flyer {
    position: absolute;
    width: 839px;
    height: 1200px;
    left: 180.5px;
    top: -180.5px;
    transform: rotate(90deg);
    transform-origin: center center;
    color: var(--paper);
    text-align: center;
  }
  .monogram {
    position: absolute;
    top: 4px;
    left: 0;
    width: 100%;
    margin: 0;
    font-family: "Oswald", sans-serif;
    font-weight: 700;
    font-size: 176px;
    line-height: 200px;
    letter-spacing: -6px;
    color: var(--mono-light);
  }
  .monogram-ring {
    display: inline-block;
    width: 26px;
    height: 26px;
    border-radius: 50%;
    background: var(--mono-dark);
    vertical-align: middle;
    margin-left: 14px;
  }
  .director-name {
    position: absolute;
    top: 206px;
    left: 0;
    width: 100%;
    margin: 0;
    font-family: "Roboto Condensed", sans-serif;
    font-weight: 400;
    font-size: 60px;
    line-height: 64px;
    letter-spacing: 1px;
    color: var(--name-grey);
  }
  .copy {
    position: absolute;
    left: 0;
    width: 100%;
    margin: 0;
    font-family: "Oswald", sans-serif;
    font-weight: 700;
    font-size: 39px;
    letter-spacing: 3.5px;
    text-transform: uppercase;
  }
  .copy span { display: block; }
  .intro { top: 281px; line-height: 48px; }
  .clients { top: 572px; line-height: 46.5px; }
  .services { top: 912px; line-height: 45px; }
  .rule {
    position: absolute;
    height: 0;
    border-top: 2px solid var(--paper);
  }
  .rule-one { top: 563px; left: 555px; width: 90px; }
  .rule-two { top: 902px; left: 573px; width: 107px; }
  .rule-three { top: 1098px; left: 620px; width: 60px; }
  .contact {
    position: absolute;
    top: 1100px;
    left: 0;
    width: 100%;
    margin: 0;
    font-family: "Oswald", sans-serif;
    font-weight: 700;
    font-size: 33px;
    line-height: 45px;
    letter-spacing: 2px;
  }
  .contact span { display: block; }
</style>
</head>
<body>
  <main class="canvas">
    <article class="flyer">
      <p class="monogram">BV<span class="monogram-ring"></span></p>
      <h1 class="director-name">BERTRAND VELLACOTT</h1>

      <p class="copy intro">
        <span>Professional</span>
        <span>Film</span>
        <span>and Music</span>
        <span>Video Director</span>
        <span>With Over</span>
        <span>10 Years Experience</span>
      </p>
      <div class="rule rule-one"></div>

      <p class="copy clients">
        <span>Client List Includes:</span>
        <span>714, Marwick, Pale Harbours,</span>
        <span>Bramblegate, The Lanterns, Blue Oak,</span>
        <span>Tamsin-Jo, Nell Maris,</span>
        <span>QRV, Willowtree</span>
        <span>Music Group,</span>
        <span>Dominic Plaskett, Kestrels</span>
      </p>
      <div class="rule rule-two"></div>

      <p class="copy services">
        <span>HD, Super 8,</span>
        <span>Live DVD,</span>
        <span>Promo Reels and Videos</span>
        <span>On Time and On Budget</span>
      </p>
      <div class="rule rule-three"></div>

      <p class="contact">
        <span>www.clipvaultia.com/bertvella</span>
        <span>bertrandvellacott@mailzephra.com</span>
      </p>
    </article>
  </main>
</body>
</html>
```